Stem Cell Facial

B0 Paper Size Poster for the Window. We are a high end Beauty Salon / Day Spa in Sydney NSW Australia.
Must be Organic looking but also attract attention. Must be modern, contemporary, clean and bold. Must our Salon Logo (velourine) (attached). The other image attached can be used, but are more of an indication of the desired look and feel. The word doc contains words that must to be used. Image of female face experiencing a beauty treatment could be used.
The Poster should be in Portrait (not Landscape)
Beauty Salon

```html
<!DOCTYPE html>
<html lang="en">
<head>
<meta charset="utf-8">
<title>Velourine Salon &amp; Spa – Stem Cell Facial Offer</title>
<link href="https://fonts.googleapis.com/css2?family=Jost:wght@300;400;500;600;700&family=Oswald:wght@400&display=swap" rel="stylesheet">
<style>
  :root {
    --charcoal: #3a3a3c;
    --ink: #1e1e1f;
    --leaf: #9bc73b;
    --leaf-dark: #7fa92a;
    --crimson: #c0200e;
    --crimson-dark: #8f1608;
    --paper: #ffffff;
    --mist: #f1f1f1;
  }
  * { margin: 0; padding: 0; box-sizing: border-box; }
  html, body {
    width: 1169px; height: 1200px; overflow: hidden;
    background: var(--paper);
    font-family: "Jost", sans-serif;
  }
  .poster {
    position: relative; width: 1169px; height: 1200px;
    background: var(--paper);
  }
  .panel {
    position: absolute; left: 19px; top: 19px; width: 1131px; height: 1163px;
    background: var(--charcoal); overflow: hidden;
  }
  .artwork { position: absolute; left: 0; top: 0; }
  .headline-ribbon {
    position: absolute; left: 34px; top: 19px; width: 236px; height: 581px;
    color: var(--paper); text-align: center;
  }
  .headline-ribbon svg { position: absolute; inset: 0; }
  .ribbon-copy { position: relative; padding-top: 36px; }
  .treatment-title { font-weight: 300; font-size: 31px; line-height: 37px; letter-spacing: 0.3px; }
  .dotted-rule { width: 210px; margin: 0 auto; border-top: 3px dotted var(--paper); }
  .treatment-title + .dotted-rule { margin-top: 30px; }
  .special-offer { font-weight: 700; font-size: 50px; line-height: 61px; margin: 28px 0 30px; }
  .tagline { font-weight: 300; font-size: 24px; line-height: 31px; margin-top: 30px; }
  .tagline strong { font-weight: 700; }

  .offer { position: absolute; }
  .offer svg { position: absolute; left: 0; top: 0; overflow: visible; }
  .offer-text { position: absolute; color: var(--paper); white-space: nowrap; }

  .facials-head { left: 141px; top: 627px; font-weight: 600; font-size: 37px; line-height: 46px; }
  .facials-head .count { font-size: 58px; font-weight: 700; vertical-align: -3px; }
  .facials-price { left: 92px; top: 780px; font-weight: 700; font-size: 76px; line-height: 88px; }
  .price-cents { font-size: 40px; vertical-align: 30px; margin-left: 4px; }
  .facials-save { left: 103px; top: 887px; font-weight: 600; font-size: 35px; line-height: 44px; }

  .bonus-head { left: 437px; top: 832px; font-weight: 700; font-size: 40px; line-height: 50px; }
  .bonus-price { left: 450px; top: 893px; font-weight: 700; font-size: 66px; line-height: 86px; }
  .bonus-price .price-cents { font-size: 36px; vertical-align: 26px; }
  .bonus-item { left: 424px; width: 272px; top: 988px; text-align: center; font-weight: 600; font-size: 37px; line-height: 45px; }

  .stock-note {
    position: absolute; left: 30px; top: 1168px;
    transform: rotate(-90deg); transform-origin: left top;
    color: var(--paper); font-weight: 400; font-size: 33px; white-space: nowrap;
  }

  .brand { position: absolute; left: 733px; top: 968px; width: 400px; }
  .brand-name {
    color: var(--leaf); font-weight: 600; font-size: 80px; line-height: 92px;
    letter-spacing: -2px; text-align: center;
  }
  .brand-rule { border-top: 2px solid #8d8d8f; margin-top: 2px; }
  .brand-sub {
    color: var(--paper); font-weight: 600; font-size: 25px; line-height: 34px;
    letter-spacing: 18.5px; text-align: center; white-space: nowrap;
  }
  .contact { position: absolute; left: 733px; top: 1108px; display: flex; align-items: center; gap: 16px; }
  .phone-icon { width: 56px; height: 56px; flex: none; }
  .phone-number {
    font-family: "Oswald", sans-serif; color: var(--leaf); font-size: 64px;
    line-height: 64px; letter-spacing: 5px; white-space: nowrap;
  }
</style>
</head>
<body>
<main class="poster">
  <div class="panel"></div>

  <svg class="artwork" width="1169" height="1200" viewBox="0 0 1169 1200">
    <defs>
      <linearGradient id="photoTone" x1="0" y1="0" x2="1" y2="1">
        <stop offset="0" stop-color="#c9c6b8"/>
        <stop offset="0.35" stop-color="#8fa07a"/>
        <stop offset="0.6" stop-color="#b98e6e"/>
        <stop offset="1" stop-color="#6e6a45"/>
      </linearGradient>
    </defs>
    <path class="photo-frame" d="M290 19 H1150 V972 C780 955 400 700 290 19 Z" fill="var(--mist)"/>
    <path class="hero-photo" role="img" aria-label="Photo of a woman wearing a crown of green leaves, resting her arms on the edge of a spa pool"
          d="M307 19 H1150 V893 C800 875 440 640 307 19 Z" fill="url(#photoTone)"/>
  </svg>

  <section class="headline-ribbon">
    <svg width="236" height="581" viewBox="0 0 236 581">
      <polygon points="0,0 236,0 236,581 118,519 0,581" fill="var(--leaf)"/>
    </svg>
    <div class="ribbon-copy">
      <h1 class="treatment-title">ANTI AGEING<br>FACIAL<br>REJUVENATION</h1>
      <div class="dotted-rule"></div>
      <p class="special-offer">SPECIAL<br>OFFER!!</p>
      <div class="dotted-rule"></div>
      <p class="tagline">EXPERIENCE THE<br><strong>POWER OF PLANT</strong><br>STEM CELLS</p>
    </div>
  </section>

  <div class="offer offer-facials">
    <svg width="1169" height="1200">
      <polygon points="205,940 308,940 205,990" fill="var(--crimson)"/>
      <polygon points="205,960 248,960 248,1024" fill="var(--leaf)"/>
      <path d="M92 649 L124 668 V700 H385 V924 Q385 944 367 944 H110 Q92 944 92 924 Z" fill="var(--leaf)"/>
      <path d="M124 630 Q124 620 136 620 H375 Q387 620 387 632 V800 L320 748 H124 Z" fill="var(--ink)"/>
      <polygon points="387,778 404,778 404,871 387,885" fill="var(--crimson-dark)"/>
      <rect x="77" y="778" width="327" height="94" fill="var(--crimson)"/>
    </svg>
    <p class="offer-text facials-head"><span class="count">2</span> STEM CELL<br>FACIALS FOR</p>
    <p class="offer-text facials-price">$249.<span class="price-cents">99</span></p>
    <p class="offer-text facials-save">SAVE OVER $50</p>
  </div>

  <div class="offer offer-bonus">
    <svg width="1169" height="1200">
      <polygon points="526,1070 629,1070 526,1164" fill="var(--crimson)"/>
      <rect x="425" y="817" width="274" height="272" rx="14" fill="var(--leaf)"/>
      <polygon points="410,894 425,882 425,894" fill="var(--crimson-dark)"/>
      <rect x="410" y="894" width="306" height="90" fill="var(--crimson)"/>
    </svg>
    <p class="offer-text bonus-head">BONUS FREE</p>
    <p class="offer-text bonus-price">$89.<span class="price-cents">95*</span></p>
    <p class="offer-text bonus-item">STEM CELL<br>EYE CREAM</p>
  </div>

  <p class="stock-note">*while stocks last</p>

  <div class="brand">
    <p class="brand-name">velourine</p>
    <div class="brand-rule"></div>
    <p class="brand-sub">salon &amp; spa</p>
  </div>

  <div class="contact">
    <svg class="phone-icon" viewBox="0 0 58 58" aria-label="Phone">
      <rect width="58" height="58" rx="9" fill="var(--leaf)"/>
      <path d="M20 12 L27 12 L29 22 L24 26 Q27 35 33 40 L38 35 L47 38 L47 45 Q46 49 41 49 Q26 47 16 32 Q11 22 13 16 Q15 12 20 12 Z" fill="var(--charcoal)"/>
    </svg>
    <p class="phone-number">9000 4821</p>
  </div>
</main>
</body>
</html>
```